Business Card for Pottery and Jewellery Designer

A new business card design is needed to accompany a newly launching pottery and jewellery website. The company logo has been attached for use. The company is called Glazewick Studio. For a sense of the vibe please see the website (it is currently under construction but this way you'll get a feel for the style) www.GlazewickStudio.com

The website font is Pontano Sans for the body of the text with Overlock for headers.

The overall look should be clean and elegant. The back side can have just the logo. The front side should have a smaller logo and the following details displayed:

Glazewick Studio
Designer: Hollis Marrow
Phone: xxx.xxx.xxxx
Email: Designer@GlazewickStudio.com

The structure of displaying this is completely up to you. Different layouts and creative methods of displaying contact info are welcome as long as it stays clean/uncluttered.

No product photographs are to be included in the design as the catalogue changes quickly.

Colour preferences lean towards elegant and understated (charcoal grey, dark navy blue etc.)

Please let me know if you have any further questions or further details required.

Target Market(s)

Target market is 30+ year old women

Industry/Entity Type

Construction

Colors
ffffff
1b1b1b
474747
d9d9d9
fafafa
0355a3

Requirements
Must have
• The submissions so far have looked very typical and don't stand out right now. They're also all in navy with very little variation. I'm looking for something that stands out a it more while still being clean-looking.
Nice to have
• I've attached a few design samples and an idea for a backdrop. It would be great to see some designs in black, white, and grey with only a hint of color.
Should not have
• Product Images

```html
<!DOCTYPE html>
<html lang="en">
<head>
<meta charset="utf-8">
<title>Glazewick Studio – Business Card</title>
<link rel="stylesheet" href="https://fonts.googleapis.com/css2?family=Play:wght@400;700&display=swap">
<style>
  :root {
    --band: #1b1b1b;
    --band-shade: #000000;
    --accent: #0355a3;
    --white: #ffffff;
    --paper: #fafafa;
    --paper-shade: #d9d9d9;
    --ink: #474747;
    --backdrop: #e6e6e6;
  }
  * { box-sizing: border-box; margin: 0; padding: 0; }
  html, body {
    width: 1200px; height: 1053px; overflow: hidden;
    background: var(--backdrop);
    font-family: "Play", sans-serif;
  }
  .card {
    position: absolute; left: 190px;
    width: 820px; height: 468px;
    background: radial-gradient(ellipse at 30% 30%, var(--white) 0%, var(--paper) 55%, var(--paper-shade) 100%);
    box-shadow: 0 8px 24px rgba(0,0,0,.22);
    overflow: hidden;
  }
  .card-back { top: 30px; }
  .card-front { top: 538px; }

  /* back side */
  .back-band {
    position: absolute; left: 0; width: 100%; background: var(--band);
  }
  .back-band-top { top: 0; height: 70px; }
  .back-band-mid { top: 172px; height: 100px; }
  .back-address {
    position: absolute; left: 90px; top: 380px;
    display: flex; align-items: center; gap: 14px;
    color: var(--ink); font-size: 21px; letter-spacing: 1px;
  }
  .back-address svg { width: 23px; height: 30px; fill: var(--accent); }

  /* front side */
  .brand {
    position: absolute; left: 123px; top: 43px;
    display: flex; align-items: center; gap: 18px;
  }
  .brand-mark {
    width: 78px; height: 78px; border-radius: 50%;
    background: var(--accent);
  }
  .brand-name {
    color: var(--band); font-size: 28px; font-weight: 400;
    letter-spacing: 4px; text-transform: uppercase; line-height: 1.1;
  }
  .name-ribbon {
    position: absolute; left: 0; top: 146px; width: 460px; height: 123px;
  }
  .person {
    position: absolute; left: 90px; top: 161px; color: var(--white);
    text-transform: uppercase;
  }
  .person-name { font-size: 28px; font-weight: 700; letter-spacing: 1px; }
  .person-role { font-size: 20px; letter-spacing: 1px; margin-top: 4px; }
  .contact {
    position: absolute; left: 500px; top: 161px; list-style: none;
    color: var(--ink); font-size: 17px;
  }
  .contact li { display: flex; align-items: center; gap: 12px; height: 31px; white-space: nowrap; }
  .contact svg { width: 18px; height: 18px; fill: var(--accent); flex: none; }
  .contact .small { font-size: 15px; }
  .footer-band {
    position: absolute; left: 0; bottom: 0; width: 100%; height: 123px;
    background: var(--band);
    display: flex; align-items: center; gap: 13px; padding-left: 115px;
    color: var(--white); font-size: 21px; letter-spacing: 1px;
  }
  .footer-band svg { width: 23px; height: 30px; fill: var(--white); }
</style>
</head>
<body>
  <section class="card card-back" aria-label="Back of card">
    <div class="back-band back-band-top"></div>
    <div class="back-band back-band-mid"></div>
    <div class="back-address">
      <svg viewBox="0 0 24 32"><path d="M12 0a12 12 0 0 0-12 12c0 9 12 20 12 20s12-11 12-20A12 12 0 0 0 12 0zm0 7a5 5 0 1 1 0 10 5 5 0 0 1 0-10z"/></svg>
      <span>214,KR,Elm Road, 2nd building Street e.</span>
    </div>
  </section>

  <section class="card card-front" aria-label="Front of card">
    <div class="brand">
      <div class="brand-mark"></div>
      <div class="brand-name">Glazewick<br>Studio</div>
    </div>

    <svg class="name-ribbon" viewBox="0 0 560 150">
      <polygon points="0,0 500,0 500,18 540,18 520,70 540,122 500,122 500,104 0,104" fill="var(--band)"/>
      <polygon points="500,104 500,122 470,104" fill="var(--band-shade)"/>
    </svg>
    <div class="person">
      <div class="person-name">Hollis Marrow</div>
      <div class="person-role">General Manager</div>
    </div>

    <ul class="contact">
      <li>
        <svg viewBox="0 0 24 24"><path d="M6 2l4 4-2 3c1 3 4 6 7 7l3-2 4 4-3 4C10 22 2 14 2 5z"/></svg>
        604 555 0142
      </li>
      <li>
        <svg viewBox="0 0 24 24"><path d="M7 1h10a2 2 0 0 1 2 2v18a2 2 0 0 1-2 2H7a2 2 0 0 1-2-2V3a2 2 0 0 1 2-2zm0 3v14h10V4z"/></svg>
        604 555 0187
      </li>
      <li>
        <svg viewBox="0 0 24 24"><path d="M6 2h9l3 3v5h3v12H3V10h3zm2 2v6h8V6h-2V4zM6 14v2h3v-2zm5 0v2h3v-2zm5 0v2h3v-2z"/></svg>
        604 555 0163
      </li>
      <li class="small">
        <svg viewBox="0 0 24 24"><path d="M2 5h20v14H2zm2 2v.5l8 5.5 8-5.5V7zm0 3v7h16v-7l-8 5.5z"/></svg>
        Designer@GlazewickStudio.com
      </li>
      <li class="small">
        <svg viewBox="0 0 24 24"><path d="M12 2a10 10 0 1 0 0 20 10 10 0 0 0 0-20zm-1 2.1V7H7.6A8 8 0 0 1 11 4.1zm2 0A8 8 0 0 1 16.4 7H13zM6.6 9H11v2H4.1a8 8 0 0 1 .5-2zm6.4 0h4.4l.5 2H13zM4.1 13H11v2H5.6a8 8 0 0 1-1.5-2zm8.9 0h6.9a8 8 0 0 1-1.5 2H13zm-5.4 4H11v2.9A8 8 0 0 1 7.6 17zm5.4 0h3.4a8 8 0 0 1-3.4 2.9z"/></svg>
        www.GlazewickStudio.com
      </li>
    </ul>

    <div class="footer-band">
      <svg viewBox="0 0 24 32"><path d="M12 0a12 12 0 0 0-12 12c0 9 12 20 12 20s12-11 12-20A12 12 0 0 0 12 0zm0 7a5 5 0 1 1 0 10 5 5 0 0 1 0-10z"/></svg>
      <span>214,KR,Elm Road, 2nd building Street e.</span>
    </div>
  </section>
</body>
</html>
```